LANDCAPE Business Card Design

We need a business card design close to what we are sending you, just more professional. We are a landscape management company located on Topsail Island so an island theme would be great. We would like to stay with a black background and bright green lettering. Something to stand out.

Target Market(s)

Commercial and private property owners

Industry/Entity Type

Landscape

Contact Information for Business Card

BRAMBLEWORKS TURF MANAGEMENT, LLC,CULTIVATE YOUR PRIVATE RETREAT, MILES HARDT 555-014-3871, DEAN PULASKI 555-019-6204

Font styles to use
Sans Serif

```html
<!DOCTYPE html>
<html lang="en">
<head>
<meta charset="utf-8">
<title>Brambleworks Turf Management – Business Card</title>
<link rel="stylesheet" href="https://fonts.googleapis.com/css2?family=Oswald:wght@500&family=Raleway:wght@400;500&family=Arimo:wght@400&display=swap">
<style>
  :root {
    --page-bg: #ffffff;
    --card-black: #000000;
    --pattern-mid: #3a3a3a;
    --pattern-dark: #0b0b0b;
    --frame-green-light: #46c04e;
    --frame-green-dark: #1d8a37;
    --brand-green: #2fa545;
    --name-green: #2c9c47;
    --silver-light: #f2f2f2;
    --silver-dark: #9a9a9a;
    --phone-white: #ffffff;
  }
  * { margin: 0; padding: 0; box-sizing: border-box; }
  html, body {
    width: 1200px; height: 900px; overflow: hidden;
    background: var(--page-bg);
  }
  .business-card {
    position: absolute;
    left: 126px; top: 157px;
    width: 948px; height: 586px;
    background: var(--card-black);
    overflow: hidden;
  }
  .damask-field {
    position: absolute; inset: 0;
    background: radial-gradient(ellipse 55% 60% at 50% 45%, var(--pattern-mid) 0%, #1c1c1c 55%, var(--pattern-dark) 85%, var(--card-black) 100%);
  }
  .green-frame {
    position: absolute;
    left: 23px; top: 27px; right: 23px; bottom: 23px;
    border: 7px solid var(--frame-green-light);
    border-image: linear-gradient(135deg, var(--frame-green-light), var(--frame-green-dark)) 1;
  }
  .tagline {
    position: absolute; left: 0; right: 0; top: 64px;
    text-align: center;
    font-family: "Oswald", sans-serif; font-weight: 500;
    font-size: 25px; letter-spacing: 15px; line-height: 34px;
    padding-left: 15px;
    color: var(--silver-light);
    background: linear-gradient(180deg, var(--silver-light) 30%, var(--silver-dark));
    -webkit-background-clip: text; background-clip: text;
    -webkit-text-fill-color: transparent;
  }
  .brand-lockup {
    position: absolute; left: 0; right: 0; top: 226px;
    display: flex; flex-direction: column; align-items: center;
  }
  .brand-name-row {
    display: flex; align-items: center; gap: 18px;
  }
  .brand-name {
    font-family: "Raleway", sans-serif; font-weight: 500;
    font-size: 70px; letter-spacing: 1px; line-height: 1;
    color: var(--brand-green);
  }
  .brand-dot {
    width: 26px; height: 26px; border-radius: 50%;
    background: var(--brand-green);
  }
  .brand-descriptor {
    margin-top: 22px;
    font-family: "Raleway", sans-serif; font-weight: 400;
    font-size: 39px; letter-spacing: 7px; line-height: 1;
    padding-left: 7px;
    color: var(--silver-light);
    background: linear-gradient(180deg, var(--silver-light) 35%, var(--silver-dark));
    -webkit-background-clip: text; background-clip: text;
    -webkit-text-fill-color: transparent;
  }
  .contact {
    position: absolute; top: 450px;
    font-family: "Arimo", sans-serif; font-weight: 400;
  }
  .contact-left { left: 55px; text-align: left; }
  .contact-right { right: 53px; text-align: right; }
  .contact-name {
    font-size: 29px; line-height: 1; color: var(--name-green);
  }
  .contact-phone {
    margin-top: 14px;
    font-size: 30px; line-height: 1; color: var(--phone-white);
  }
</style>
</head>
<body>
  <div class="business-card">
    <div class="damask-field" role="img" aria-label="Dark grey floral damask pattern glowing behind the company name"></div>
    <div class="green-frame"></div>

    <p class="tagline">CULTIVATE YOUR PRIVATE RETREAT</p>

    <div class="brand-lockup">
      <div class="brand-name-row">
        <span class="brand-name">BRAMBLEWORKS</span>
        <span class="brand-dot"></span>
      </div>
      <p class="brand-descriptor">TURF MANAGEMENT, LLC</p>
    </div>

    <div class="contact contact-left">
      <p class="contact-name">MILES HARDT</p>
      <p class="contact-phone">555-014-3871</p>
    </div>
    <div class="contact contact-right">
      <p class="contact-name">DEAN PULASKI</p>
      <p class="contact-phone">555-019-6204</p>
    </div>
  </div>
</body>
</html>
```